We need a flyer for our company. We test drugs, laser, LED or other light sources for phototoxicity on healthy volunteers.
You can use our website for an idea or imagine www.lumivarex.co.uk
Lumivarex has a well-established reputation in the field of drug- and chemical-induced phototoxicity and expertise in clinical studies of photoprotective agents, such as nutraceuticals and antioxidants and light-based device development and application. The team at Lumivarex has an international reputation in the field of UV and visible light measurement and our team has a truly multidisciplinary nature, with professionals including physicians, medical physicists, biochemists, technicians and nurses.

Target Market(s)

any pharmaceutical or cosmetical company

Industry/Entity Type

Cosmetic

Font styles to use
Serif

Colors

Designer to choose colors to be used in the design.

Requirements
Must have
• Clinical studies:
• Phototoxicity
• Photoallergy to topical agents
• Photoprotection by oral or topical agents
• Light-based devices
• Laboratory studies:
• Photosafety and photoxicity
• Photophysics and light source evaluation
Nice to have
• Can you reduce the amount of text and concentrate on this point?
• First page:
• • Lumivarex has a well-established reputation in the field of drug- and chemical-induced phototoxicity and expertise in clinical studies of photoprotective agents:
• such as nutraceuticals
• and antioxidants
• and light-based device development and application.
• • The team at Lumivarex has an international reputation in the field of UV and visible light measurement and our team has a truly multidisciplinary nature, with professionals including physicians, medical physicists, biochemists, technicians and nurses
• Second page:
• Clinical studies
• Phototoxicity
• Light-based devices
• Laboratory studies

```html
<!DOCTYPE html>
<html lang="en">
<head>
<meta charset="utf-8">
<title>Lumivarex – Phototoxicity Studies Flyer</title>
<link href="https://fonts.googleapis.com/css2?family=Source+Serif+4:opsz,wght@8..60,400;8..60,600;8..60,700&display=swap" rel="stylesheet">
<style>
:root{
  --navy:#0e3a66;
  --navy-deep:#0a2f55;
  --sky:#72cbef;
  --grey-bar:#b9b9b9;
  --footer:#333435;
  --white:#ffffff;
  --ink:#1d1d1d;
  --body-light:#e6eef6;
  --rule:#3a6590;
}
*{margin:0;padding:0;box-sizing:border-box}
html,body{width:1200px;height:780px;overflow:hidden;background:#fff}
body{font-family:'Source Serif 4',Georgia,serif;position:relative}
.page{position:absolute;top:53px;width:480px;height:681px;background:var(--navy);overflow:hidden}
.page--front{left:106px}
.page--back{left:623px}
.block{position:absolute}
.photo{position:absolute}
.label-bar{position:absolute;height:17px;font-size:11.5px;letter-spacing:-.1px;color:var(--white);padding-left:20px;line-height:17px;text-transform:uppercase}
.label-bar--sky{background:var(--sky)}
.label-bar--grey{background:var(--grey-bar)}
.brand{position:absolute;left:15px;top:19px;width:122px;height:32px;background:var(--navy);border-radius:3px;display:flex;align-items:center;gap:7px;padding-left:10px}
.brand__mark{width:12px;height:12px;background:var(--white)}
.brand__name{font-size:14.5px;font-weight:700;color:var(--white)}
.headline{position:absolute;left:20px;top:232px;font-size:10.2px;font-weight:600;letter-spacing:-.3px;color:var(--white);text-transform:uppercase;white-space:nowrap}
.about{position:absolute;left:0;top:255px;width:240px;height:195px;background:var(--white)}
.about__text{position:absolute;left:20px;top:36px;width:214px;font-size:9.3px;line-height:11.6px;color:var(--ink);letter-spacing:-.15px}
.contact{position:absolute;left:0;top:605px;width:240px;height:76px;background:var(--footer);color:#fff;font-size:8.3px;line-height:10.2px}
.contact__addr{position:absolute;left:20px;top:9px}
.contact__lines{position:absolute;left:121px;top:9px}
.study{position:absolute;left:258px;width:214px;color:var(--white)}
.study h3,.lab h3{font-size:12.2px;font-weight:400;letter-spacing:-.2px;margin-bottom:5px;white-space:nowrap}
.study p,.lab p,.volunteer p,.services p{font-size:9.3px;line-height:11.7px;letter-spacing:-.15px;color:var(--body-light)}
.divider{position:absolute;left:240px;width:240px;height:1px;background:var(--rule)}
.lab{position:absolute;top:46px;width:208px;color:var(--white)}
.volunteer{position:absolute;left:20px;width:215px;color:var(--white)}
.volunteer h4{font-size:9.5px;font-weight:600;text-transform:uppercase;line-height:11.5px;margin-bottom:12px}
.volunteer p+p{margin-top:11.5px}
.services{position:absolute;left:246px;top:373px;width:222px}
.services p+p{margin-top:11.5px}
</style>
</head>
<body>

<section class="page page--front">
  <div class="photo" style="left:0;top:0;width:480px;height:224px;background:linear-gradient(135deg,#c8d3de 0%,#eef1f4 45%,#b9bec4 75%,#6f7378 100%)" role="img" aria-label="Clinical treatment room with a light source unit and examination couch"></div>
  <div class="brand"><span class="brand__mark"></span><span class="brand__name">Lumivarex</span></div>
  <h1 class="headline">Evidence-based methodology for studying phototoxicity in healthy volunteers</h1>

  <div class="about">
    <div class="label-bar label-bar--sky" style="left:0;top:16px;width:210px">About us</div>
    <p class="about__text"><b>Lumivarex Ltd.</b> was launched in 2008 but drug phototoxicity work has been undertaken on this site within the Northfield Photobiology Unit in Kelbridge, Scotland since the 1980s. Its sole shareholder is the Lightcare Trust, a charitable organisation devoted to the promotion of dermatological research, education and clinical care. All funds generated through Lumivarex are used for further clinical research and educational activities for patient care and benefit. Lumivarex is a limited company independent of the Public Health Service.</p>
  </div>
  <div class="photo" style="left:0;top:450px;width:240px;height:155px;background:linear-gradient(180deg,#6b4a3a 0%,#8a6a55 55%,#5f6470 100%)" role="img" aria-label="The Lumivarex team standing in front of a library bookcase"></div>
  <div class="contact">
    <div class="contact__addr">Lumivarex Ltd.<br>Photobiology Unit<br>Harrowmere Hospital<br>Kelbridge<br>KB1 4QX</div>
    <div class="contact__lines">+44(0)1632 960120<br>Fax:+44(0)1632 960785<br><br>Email:<br>info@lumivarex.co.uk</div>
  </div>

  <div class="label-bar label-bar--grey" style="left:240px;top:271px;width:221px">Clinical studies</div>
  <div class="study" style="top:296px">
    <h3>Phototoxicity</h3>
    <p>Our purpose in clinical phototoxicity studies is to detect whether or not an investigational drug, laser, Light Emitting Diode (LED) or other light source can potentially cause cutaneous phototoxicity in man.</p>
  </div>
  <div class="divider" style="top:386px"></div>
  <div class="study" style="top:396px">
    <h3>Photoallergy to topical agents</h3>
    <p>Phototoxicity may also be an issue for drugs and chemicals that absorb UV and/or visible radiation and are applied topically, or accumulate in the skin following administration by other routes.</p>
  </div>
  <div class="divider" style="top:474px"></div>
  <div class="study" style="top:484px">
    <h3>Photoprotection by oral or topical agents</h3>
    <p>We have experience and expertise in undertaking healthy volunteer studies of potentially photoprotective compounds, such as nutraceuticals and antioxidants, which may be investigated through either the systemic or topical route of delivery.</p>
  </div>
  <div class="divider" style="top:575px"></div>
  <div class="study" style="top:584px">
    <h3>Light-based devices</h3>
    <p>We have expertise and experience in the field of assessment and clinical trials of light-based diagnostic and therapeutic devices and dedicated photophysicists are core members of the Lumivarex team.</p>
  </div>
</section>

<section class="page page--back">
  <div class="label-bar label-bar--grey" style="left:0;top:14px;width:234px">Laboratory studies</div>
  <div class="block" style="left:246px;top:0;width:1px;height:130px;background:var(--rule)"></div>
  <div class="lab" style="left:31px">
    <h3>Photosafety and photoxicity</h3>
    <p>Our purpose in clinical phototoxicity studies is to detect whether or not an investigational drug, laser, Light Emitting Diode (LED) or other light source can potentially cause cutaneous phototoxicity in man.</p>
  </div>
  <div class="lab" style="left:258px;width:214px">
    <h3>Photophysics and light source evaluation</h3>
    <p>Our purpose in clinical phototoxicity studies is to detect whether or not an investigational drug, laser, Light Emitting Diode (LED) or other light source can potentially cause cutaneous phototoxicity in man.</p>
  </div>

  <div class="block" style="left:0;top:130px;width:481px;height:9px;background:var(--white)"></div>
  <div class="photo" style="left:0;top:139px;width:481px;height:187px;background:linear-gradient(120deg,#0a0f24 0%,#1a2460 40%,#6a6ff0 70%,#d9dcf5 100%)" role="img" aria-label="Technician working at a laboratory bench lit by a blue-violet light source"></div>
  <div class="block" style="left:0;top:326px;width:481px;height:9px;background:var(--white)"></div>

  <div class="label-bar label-bar--grey" style="left:0;top:350px;width:234px">How to be a study volunteer</div>
  <div class="volunteer" style="top:385px">
    <h4>Do I get reimbursed?</h4>
    <p>Yes. Lumivarex pays volunteers for their participation in drug trials/studies and provides local transport or reimburses travel expenses.</p>
    <p>The reimbursement for each study varies according to the time volunteers devote to the study, the number of visits they need to make and the inconvenience of the schedule. An independent Research Ethics Committee approves the payments we make to volunteers for trial participation. Study payments are made at the end of the study, after the final visit to the laboratories, by cheque in the volunteer's name.</p>
  </div>
  <div class="volunteer" style="top:585px">
    <h4>What are the trials for and<br>who benefits?</h4>
    <p>These studies assist the development of new drugs and medications. Any profits earned by Lumivarex in conducting these studies are used in research and educational activities for the benefit of patients.</p>
  </div>

  <div class="block" style="left:240px;top:335px;width:241px;height:182px;background:var(--navy-deep)"></div>
  <div class="label-bar label-bar--sky" style="left:240px;top:350px;width:221px;padding-left:7px">Our services</div>
  <div class="services">
    <p>The Lumivarex Team has developed substantial expertise in advising on the need or otherwise for phototoxicity studies of new drugs and compounds, as well as photoprotection studies.</p>
    <p>Clinical phototoxicity trials test drugs or products supplied by industry in healthy volunteers. The results are analysed and reported back to the trial sponsor.</p>
  </div>
  <div class="block" style="left:240px;top:517px;width:241px;height:9px;background:var(--white)"></div>
  <div class="photo" style="left:240px;top:526px;width:241px;height:155px;background:linear-gradient(135deg,#2a1c12 0%,#5a3a22 50%,#1a1a1c 100%)" role="img" aria-label="Hands holding a thermal imaging camera"></div>
</section>

</body>
</html>
```